Business Card Design

We need a business card designed for our new company. Prefer a black card with white logo & writing.

Contact Information for Business Card

Dale Pickett, address: 7-4417 Larchmere Avenue, Abbotsford, BC, V3K 2R9, Office Phone: 604-555-0172, Cell: 604-555-0138, Email: dale@kelsoncoatworks.ca

Colors

Designer to choose only greyscale colors for use in the design.

```html
<!DOCTYPE html>
<html lang="en">
<head>
<meta charset="UTF-8">
<title>Kelson Coatworks – Business Card</title>
<link href="https://fonts.googleapis.com/css2?family=Arimo:wght@400;700&display=swap" rel="stylesheet">
<style>
  :root {
    --backdrop: #d2d2d2;
    --card-dark: #343336;
    --stripe-tone: #3f4043;
    --band-grey: #a0a0a0;
    --fold-grey: #8a8a8a;
    --paper: #ffffff;
    --ink-light: #ffffff;
    --ink-muted: #a9a9a9;
    --ink-dark: #1e1e1e;
  }
  * { margin: 0; padding: 0; box-sizing: border-box; }
  html, body {
    width: 1200px; height: 900px; overflow: hidden;
    background: var(--backdrop);
    font-family: "Arimo", Arial, sans-serif;
  }
  .card {
    position: absolute;
    top: 320px;
    width: 424px; height: 256px;
    overflow: hidden;
  }
  .card--front { left: 139px; background: var(--card-dark); }
  .card--back { left: 664px; background: var(--card-dark); }

  .card__art { position: absolute; inset: 0; }

  .brand-name {
    position: absolute;
    left: 0; right: 0;
    text-align: center;
    font-family: "Arimo", Arial, sans-serif;
    font-weight: 700;
    letter-spacing: 0.5px;
    line-height: 1.05;
  }
  .card--front .brand-name { top: 60px; font-size: 24px; color: var(--ink-light); }
  .card--back .brand-name { top: 100px; width: 216px; font-size: 21px; color: var(--ink-dark); }

  .website {
    position: absolute;
    left: 0; right: 0; top: 199px;
    text-align: center;
    font-size: 8.5px;
    font-weight: 700;
    letter-spacing: 2.3px;
    color: var(--ink-muted);
  }

  .back__paper { position: absolute; left: 0; top: 0; width: 216px; height: 256px; background: var(--paper); }
  .back__stripes { position: absolute; left: 216px; top: 0; width: 23px; height: 256px; background: var(--stripe-tone); }
  .name-band {
    position: absolute; left: 205px; top: 41px; right: 0; height: 50px;
    background: var(--band-grey);
  }
  .name-band__fold { position: absolute; left: 205px; top: 91px; }
  .name-band__fold-top { position: absolute; left: 205px; top: 35px; }
  .person-name {
    position: absolute; left: 261px; top: 59px;
    font-size: 12.5px; font-weight: 700; letter-spacing: 0.6px;
    color: var(--ink-light);
  }
  .contact {
    position: absolute; left: 267px;
    display: flex; align-items: center; gap: 6px;
    font-size: 9.6px; line-height: 11.5px; color: var(--ink-muted);
  }
  .contact--address { line-height: 16px; }
  .contact__icon { width: 11px; height: 12px; flex: none; fill: var(--ink-light); }
  .contact--phone { top: 123px; }
  .contact--email { top: 162px; }
  .contact--address { top: 186px; }
</style>
</head>
<body>

<section class="card card--front" aria-label="Card front">
  <svg class="card__art" width="424" height="256" viewBox="0 0 424 256">
    <rect class="stripe-band" x="0" y="172" width="424" height="22" fill="var(--stripe-tone)" role="img" aria-label="Band of diagonal dark stripes"/>
    <path class="stripe-notch" d="M0 193 H424 V256 H0 Z" fill="var(--stripe-tone)" role="img" aria-label="Diagonal dark stripes inside the notch"/>
    <path class="lower-band" d="M0 193 H78 Q98 193 106 210 L114 225 Q120 234 134 234 H292 Q306 234 312 225 L320 210 Q328 193 348 193 H424 V256 H0 Z" fill="var(--band-grey)"/>
    <circle class="divider-dot" cx="212" cy="173" r="4.5" fill="var(--band-grey)"/>
  </svg>
  <div class="brand-name">KELSON<br>COATWORKS</div>
  <div class="website">www.kelsoncoatworks.shop</div>
</section>

<section class="card card--back" aria-label="Card back">
  <div class="back__paper"></div>
  <div class="back__stripes" role="img" aria-label="Vertical column of diagonal dark stripes"></div>
  <div class="brand-name">KELSON<br>COATWORKS</div>

  <svg class="name-band__fold-top" width="12" height="6" viewBox="0 0 12 6"><path d="M0 6 L12 0 V6 Z" fill="var(--fold-grey)"/></svg>
  <div class="name-band"></div>
  <svg class="name-band__fold" width="12" height="6" viewBox="0 0 12 6"><path d="M0 0 H12 V6 Z" fill="var(--fold-grey)"/></svg>
  <div class="person-name">Dale Pickett</div>

  <div class="contact contact--phone">
    <svg class="contact__icon" viewBox="0 0 24 24"><path d="M6.6 10.8c1.4 2.8 3.8 5.1 6.6 6.6l2.2-2.2c.3-.3.7-.4 1-.2 1.1.4 2.3.6 3.6.6.6 0 1 .4 1 1V20c0 .6-.4 1-1 1C10.6 21 3 13.4 3 4c0-.6.4-1 1-1h3.5c.6 0 1 .4 1 1 0 1.3.2 2.5.6 3.6.1.3 0 .7-.2 1z"/></svg>
    <div>604-555-0172 (Office)<br>604-555-0138 (Cell)</div>
  </div>

  <div class="contact contact--email">
    <svg class="contact__icon" viewBox="0 0 24 24"><path d="M2 5h20v14H2z M3.5 6.5 12 13l8.5-6.5" fill="var(--ink-light)" stroke="var(--card-dark)" stroke-width="1.4"/></svg>
    <div>dale@kelsoncoatworks.ca</div>
  </div>

  <div class="contact contact--address">
    <svg class="contact__icon" viewBox="0 0 24 24"><path d="M12 2a7 7 0 0 0-7 7c0 5.2 7 13 7 13s7-7.8 7-13a7 7 0 0 0-7-7zm0 9.5A2.5 2.5 0 1 1 12 6.5a2.5 2.5 0 0 1 0 5z"/></svg>
    <div>7-4417 Larchmere Avenue,<br>Abbotsford, BC, V3K 2R9</div>
  </div>
</section>

</body>
</html>
```